We are Pacific Auto Freight Traders from Japan to NewZealand

we are importing Japanese used cars from Japan to NewZealand and Motor vehicle parts trading in the world. we have company in Japan and New Zealand. we provide one stop service to import car from japan. we have two companies called PAF Ltd for car importing from japan and PAF Lubricants Ltd for car engine oil importing. also we are importing car parts under PAF Autohaus Ltd. we need logo and name card for our company. Company name is PAF LTD (Pacific Auto Freight Traders) From japan we are sourcing newer European cars and 20-30 years old special sports limited model cars importing specialist. we are not normal car importer and retailer. also we are manufacture and supplying Motor vehicle Engine oil and parts from Korea and japan to New Zealand. Engine oil and part brand name is 'Ultra Z' we would like to introduce on business card. we want to show what we are doing as car importing, selling, parts and engine oil importing.

Target Market(s)

-Car buyer(customer)
-Mechanic shop
-Car dealers
-Car industry people
-Car & parts exporter/importer
-Engine oil reseller
-parts reseller

Industry/Entity Type

Car Dealer

Contact Information for Business Card

Dale Ferro
Director
17 Brook Lane, Tokomai Flats, Auckland 0619, New Zealand
+64215093381
paf.limited@examplemail.co.nz
www.pafmotors-demo.co.nz
www.pafjapan-demo.com

Colors
ffc214
9d9d9d
0255a3

Requirements
Must have
• * PAF Motors Ltd(PAF LTD-car importing, sourcing and retailing)
• * PAF Lubricants Ltd(Engine Oil importing, sourcing and retailing)
• * PAF Autohaus Ltd(car parts and accessories importing, sourcing and retailing)
• * Ultra Z -Brand name of engine oil
• (We are wanting to make logo for PAF MOTORS and ULTRA Z MOTOR OIL)
Nice to have
• we would like to show us to our clients as professional, trustworthy, many experience. not well known in the market but unique indivisual company for clients.
Should not have
• we do not want to feel just 'car dealer' , 'importer' or normal sales

```html
<!DOCTYPE html>
<html lang="en">
<head>
<meta charset="utf-8">
<title>PAF Motors Ltd — Business Card</title>
<link rel="stylesheet" href="https://fonts.googleapis.com/css2?family=Open+Sans:wght@400;600;700&display=swap">
<style>
  :root {
    --brand-blue: #0255a3;
    --card-blue: #0a4f93;
    --brand-yellow: #ffc214;
    --brand-grey: #9d9d9d;
    --paper: #ffffff;
    --backdrop: #e8e6e2;
    --text-blue: #0a4f93;
  }
  * { box-sizing: border-box; margin: 0; padding: 0; }
  html, body { width: 1200px; height: 750px; overflow: hidden; }
  body {
    background: var(--backdrop);
    font-family: "Open Sans", Arial, sans-serif;
    position: relative;
  }
  .card {
    position: absolute;
    top: 202px;
    width: 559px;
    height: 318px;
    border-radius: 20px;
    overflow: hidden;
    background: var(--card-blue);
    box-shadow: 0 3px 8px rgba(0,0,0,0.25);
  }
  .card--front { left: 28px; }
  .card--back { left: 614px; }

  .front-shape { position: absolute; inset: 0; }

  .brand { position: absolute; color: #fff; }
  .brand__name {
    display: flex;
    align-items: center;
    gap: 10px;
    font-weight: 700;
    color: var(--paper);
    letter-spacing: 0.5px;
    white-space: nowrap;
  }
  .brand__dot {
    display: inline-block;
    border-radius: 50%;
    background: var(--brand-yellow);
  }
  .brand__tagline {
    font-weight: 400;
    color: var(--paper);
    white-space: nowrap;
  }
  .card--front .brand { left: 244px; top: 58px; }
  .card--front .brand__name { font-size: 26px; }
  .card--front .brand__dot { width: 18px; height: 18px; }
  .card--front .brand__tagline { font-size: 10.5px; margin-top: 1px; }

  .card--back .brand { left: 80px; top: 76px; }
  .card--back .brand__name { font-size: 38px; }
  .card--back .brand__dot { width: 26px; height: 26px; }
  .card--back .brand__tagline { font-size: 13.5px; margin-top: 0; }

  .contact { position: absolute; left: 34px; top: 140px; color: var(--text-blue); }
  .contact__name { font-size: 19px; font-weight: 700; letter-spacing: 0.3px; line-height: 1.1; }
  .contact__role { font-size: 13px; color: var(--brand-grey); letter-spacing: 0.5px; line-height: 1.3; }
  .contact__address { font-size: 15px; line-height: 1.3; margin-top: 8px; }
  .contact__list { list-style: none; margin-top: 14px; font-size: 15px; line-height: 18px; }
  .contact__list li { display: flex; align-items: center; gap: 7px; }
  .contact__list svg { width: 12px; height: 12px; flex: none; }

  .divisions {
    position: absolute;
    right: 38px;
    top: 184px;
    list-style: none;
    color: var(--paper);
    font-size: 12.4px;
    line-height: 15px;
    text-align: right;
  }
  .divisions li { display: flex; justify-content: flex-end; align-items: center; gap: 8px; }
  .divisions li::after {
    content: "";
    width: 9px; height: 9px;
    border-radius: 50%;
    background: #c9cbcf;
    flex: none;
  }
  .back-web {
    position: absolute;
    left: 202px;
    top: 284px;
    color: var(--paper);
    font-size: 14px;
  }
</style>
</head>
<body>

<section class="card card--front" aria-label="Business card front">
  <svg class="front-shape" viewBox="0 0 559 318" preserveAspectRatio="none" aria-hidden="true">
    <path d="M38,0 Q326,70 344,318" fill="none" stroke="var(--brand-yellow)" stroke-width="7"/>
    <path d="M24,0 Q316,72 330,318" fill="none" stroke="var(--brand-grey)" stroke-width="8"/>
    <path d="M0,0 L10,0 Q300,74 314,318 L0,318 Z" fill="var(--paper)" stroke="var(--card-blue)" stroke-width="5"/>
  </svg>

  <div class="brand">
    <div class="brand__name">PAF Motors Ltd <span class="brand__dot"></span></div>
    <div class="brand__tagline">Pacific Auto Freight Traders Limited (PAFT)</div>
  </div>

  <div class="contact">
    <div class="contact__name">DALE FERRO</div>
    <div class="contact__role">DIRECTOR</div>
    <div class="contact__address">17 Brook Lane, Tokomai Flats<br>Auckland 0619, New Zealand</div>
    <ul class="contact__list">
      <li>
        <svg viewBox="0 0 12 12" aria-hidden="true"><path d="M2.5,1 L4.5,1 L5,3.5 L3.8,4.5 Q5,7 7.5,8.2 L8.5,7 L11,7.5 L11,9.5 Q10,11 8,10.8 Q2,9 1,3 Q1,1.5 2.5,1 Z" fill="none" stroke="var(--brand-grey)" stroke-width="1"/></svg>
        +64215093381
      </li>
      <li>
        <svg viewBox="0 0 12 12" aria-hidden="true"><rect x="0.8" y="2.5" width="10.4" height="7" fill="none" stroke="var(--brand-grey)" stroke-width="1"/><path d="M0.8,2.5 L6,6.5 L11.2,2.5" fill="none" stroke="var(--brand-grey)" stroke-width="1"/></svg>
        paf.limited@examplemail.co.nz
      </li>
      <li>
        <svg viewBox="0 0 12 12" aria-hidden="true"><circle cx="6" cy="6" r="5" fill="none" stroke="var(--brand-grey)" stroke-width="1"/><ellipse cx="6" cy="6" rx="2.2" ry="5" fill="none" stroke="var(--brand-grey)" stroke-width="1"/><path d="M1,6 H11" stroke="var(--brand-grey)" stroke-width="1"/></svg>
        www.pafmotors-demo.co.nz
      </li>
    </ul>
  </div>
</section>

<section class="card card--back" aria-label="Business card back">
  <div class="brand">
    <div class="brand__name">PAF Motors Ltd <span class="brand__dot"></span></div>
    <div class="brand__tagline">Pacific Auto Freight Traders Limited (PAFT)</div>
  </div>

  <ul class="divisions">
    <li>Ultra Z -Brand name of engine oil</li>
    <li>PAF Motors Ltd(PAF LTD-car importing, sourcing and retailing)</li>
    <li>PAF Lubricants Ltd(Engine Oil importing, sourcing and retailing)</li>
    <li>PAF Autohaus Ltd(car parts and accessories importing, sourcing and retailing)</li>
  </ul>

  <div class="back-web">www.pafjapan-demo.com</div>
</section>

</body>
</html>
```